Tamkor, a service provider dedicated to improving the performance of a website

Tamkor offers optimization and performance improvement for all types of websites (showcase sites, e-commerce, ...), with the aim of improving their ranking on Vintrel and their customer transformation rate. The main benefits consist in optimizing the factors of a site. In addition, we also offer content creation (description of product sheets, services, ...), Vintrel Ads campaign management, migration version for Prestashop / Wordpress, etc. The design must be a fresh image, dynamic, why not "fun", but also serious. No favorite color, carte blanche on this point;)

```html
<!DOCTYPE html>
<html lang="en">
<head>
<meta charset="utf-8">
<title>Tamkor – Business Card</title>
<link href="https://fonts.googleapis.com/css2?family=Lato:wght@400;700;900&display=swap" rel="stylesheet">
<style>
  :root {
    --brand-blue: #3c57a4;
    --paper: #ffffff;
    --ink: #1f1f1f;
    --backdrop: #2a2a2a;
  }
  * { box-sizing: border-box; margin: 0; padding: 0; }
  html, body {
    width: 1200px; height: 878px; overflow: hidden;
    background: var(--backdrop);
    font-family: "Lato", sans-serif;
  }
  .canvas {
    position: relative; width: 1200px; height: 878px;
    display: flex; flex-direction: column; align-items: center; justify-content: center; gap: 40px;
  }
  .card {
    position: relative; width: 660px; height: 377px; overflow: hidden;
    box-shadow: 0 10px 30px rgba(0,0,0,.45);
  }
  /* Back side */
  .card--back { background: var(--brand-blue); display: flex; align-items: center; justify-content: center; }
  .card--back .wordmark { color: var(--paper); font-size: 96px; }
  .wordmark {
    font-family: "Lato", sans-serif; font-weight: 900; letter-spacing: -1px; line-height: 1;
  }
  /* Front side */
  .card--front { background: var(--paper); }
  .card--front .wordmark {
    position: absolute; left: 42px; top: 82px; color: var(--brand-blue); font-size: 92px;
  }
  .holder {
    position: absolute; right: 48px; top: 34px; text-align: right;
  }
  .holder__name {
    color: var(--brand-blue); font-weight: 900; font-size: 27px; letter-spacing: .5px; text-transform: uppercase;
  }
  .holder__role { color: var(--ink); font-size: 17px; margin-top: 2px; }
  .holder-bar {
    position: absolute; right: 12px; top: 38px; width: 18px; height: 56px; background: var(--brand-blue);
  }
  .wave { position: absolute; left: 0; top: 0; width: 660px; height: 377px; }
  .contact {
    position: absolute; right: 30px; bottom: 22px; list-style: none; text-align: right; color: var(--paper);
  }
  .contact li {
    display: flex; align-items: center; justify-content: flex-end; gap: 14px;
    font-size: 19px; line-height: 30px; letter-spacing: .3px;
  }
  .contact svg { width: 20px; height: 20px; flex: none; }
</style>
</head>
<body>
<main class="canvas">
  <section class="card card--back" aria-label="Card back">
    <span class="wordmark">Tamkor</span>
  </section>

  <section class="card card--front" aria-label="Card front">
    <svg class="wave" viewBox="0 0 660 377" aria-hidden="true">
      <path d="M0,228 C110,275 240,300 390,268 C490,246 580,232 660,252 L660,377 L0,377 Z" fill="var(--brand-blue)"/>
      <path d="M48,282 C160,302 300,268 430,236 C500,220 560,212 600,214 C540,216 470,230 400,250 C290,282 170,306 48,282 Z" fill="var(--paper)"/>
      <path d="M60,278 C180,292 310,254 430,224 C500,208 560,200 600,204 C540,206 470,218 400,236 C290,266 170,296 60,278 Z" fill="var(--brand-blue)"/>
    </svg>

    <span class="wordmark">Tamkor</span>

    <div class="holder">
      <p class="holder__name">Marc Delorme</p>
      <p class="holder__role">Founder &amp; CEO</p>
    </div>
    <span class="holder-bar"></span>

    <ul class="contact">
      <li>1234567890
        <svg viewBox="0 0 24 24" aria-hidden="true"><path fill="currentColor" d="M6.6 10.8a15 15 0 0 0 6.6 6.6l2.2-2.2a1 1 0 0 1 1-.25 11.4 11.4 0 0 0 3.6.57 1 1 0 0 1 1 1V20a1 1 0 0 1-1 1A17 17 0 0 1 3 4a1 1 0 0 1 1-1h3.5a1 1 0 0 1 1 1c0 1.25.2 2.45.57 3.6a1 1 0 0 1-.25 1Z"/></svg>
      </li>
      <li>info@yourmail.com
        <svg viewBox="0 0 24 24" aria-hidden="true"><path fill="currentColor" d="M2 5h20v14H2Zm2 2v.4l8 5.2 8-5.2V7Zm0 2.8V17h16V9.8l-8 5.2Z"/></svg>
      </li>
      <li>www.yourwebsite.com
        <svg viewBox="0 0 24 24" aria-hidden="true"><circle cx="12" cy="12" r="9" fill="none" stroke="currentColor" stroke-width="2"/><path d="M3 12h18M12 3c3 3 3 15 0 18M12 3c-3 3-3 15 0 18" fill="none" stroke="currentColor" stroke-width="1.5"/></svg>
      </li>
    </ul>
  </section>
</main>
</body>
</html>
```